Construction material supplies company business card ****

1. Full company name “K R Mortar Works Ltd”
I am after a Business card design for the company as a whole. We are better known in Solomon Islands as “K R Mortar” for short.

We are a building materials supplier of
Ready Mixed Concrete, Bricks and Blocks,
Quarry products- gravel, aggregates, sand etc.
Cement distributor/retailer of reputable brands.
Other prefab concrete products. Culverts, wave breakers, concrete retaining blocks etc.

2. Competitive Advantage over Competition: Quality, efficient, professional, dependable, reliable

3. We want people to feel trust worthy, high quality, strong when they see our brand

5. No preference to color. Maybe more sturdy and corporate. Not fancy.

Industry/Entity Type

CONSTRUCTION SUPPLY

Contact Information for Business Card

Name, Position, office phone mob phone, email

Requirements
Must have
• the company logo
Nice to have
• would like to see a mixture of designs, of with logo only and also with simple graphic designs to bring out the company whilst still have the strong sturdy professional feeling

```html
<!DOCTYPE html>
<html lang="en">
<head>
<meta charset="utf-8">
<title>K R Mortar — Business Card</title>
<link href="https://fonts.googleapis.com/css2?family=Roboto:wght@400;700&display=swap" rel="stylesheet">
<style>
  :root {
    --backdrop: #94979c;
    --navy: #0f3f66;
    --navy-deep: #0c3659;
    --paper: #efeef2;
    --ink-soft: #4a4d52;
  }
  * { box-sizing: border-box; margin: 0; padding: 0; }
  html, body { width: 1200px; height: 900px; overflow: hidden; }
  body {
    background: var(--backdrop);
    font-family: "Roboto", Arial, sans-serif;
    position: relative;
  }
  .card {
    position: absolute;
    left: 363px;
    width: 475px;
    height: 271px;
  }
  .card-front { top: 145px; background: var(--navy); }
  .card-back { top: 484px; background: var(--paper); }

  .front-pattern-area {
    position: absolute;
    inset: 0;
    background: linear-gradient(135deg, var(--navy) 0%, var(--navy-deep) 100%);
  }
  .front-wordmark {
    position: absolute;
    left: 0; right: 0; top: 50%;
    transform: translateY(-50%);
    text-align: center;
    color: #ffffff;
    font-weight: 700;
    font-size: 26px;
    letter-spacing: 2px;
  }

  .back-wordmark {
    position: absolute;
    left: 0; right: 0; top: 68px;
    display: flex;
    justify-content: center;
    align-items: center;
    gap: 10px;
    color: var(--navy);
    font-weight: 700;
    font-size: 28px;
    letter-spacing: 1.5px;
  }
  .wordmark-square {
    width: 26px; height: 26px;
    background: var(--navy);
  }

  .holder {
    position: absolute;
    right: 249px;
    top: 184px;
    text-align: right;
  }
  .holder-name {
    color: var(--navy);
    font-weight: 700;
    font-size: 15px;
    letter-spacing: 0.2px;
  }
  .holder-role {
    color: var(--ink-soft);
    font-size: 11px;
    margin-top: 3px;
  }
  .divider {
    position: absolute;
    left: 237px;
    top: 173px;
    width: 1px;
    height: 55px;
    background: var(--navy);
  }
  .contact-list {
    position: absolute;
    left: 249px;
    top: 169px;
    list-style: none;
  }
  .contact-item {
    display: flex;
    align-items: center;
    height: 15.3px;
    color: var(--ink-soft);
    font-size: 11px;
  }
  .contact-icon {
    width: 9px; height: 9px;
    margin-right: 5px;
    fill: var(--navy);
  }
</style>
</head>
<body>
  <section class="card card-front">
    <div class="front-pattern-area" role="img" aria-label="Repeating tonal navy brand pattern"></div>
    <div class="front-wordmark">K R MORTAR</div>
  </section>

  <section class="card card-back">
    <div class="back-wordmark"><span class="wordmark-square"></span><span>K R MORTAR</span></div>

    <div class="holder">
      <div class="holder-name">PETER LOWANA</div>
      <div class="holder-role">Director</div>
    </div>
    <div class="divider"></div>

    <ul class="contact-list">
      <li class="contact-item">
        <svg class="contact-icon" viewBox="0 0 10 10"><path d="M2.5 0.5h5v9h-5z M3.3 1.3v6.4h3.4V1.3z" fill-rule="evenodd"/><circle cx="5" cy="8.6" r="0.5"/></svg>
        677.746.2210
      </li>
      <li class="contact-item">
        <svg class="contact-icon" viewBox="0 0 10 10"><path d="M2 0.5l2 2.2-1 1.2c0.6 1.3 1.6 2.3 2.9 2.9l1.2-1 2.2 2-1.3 1.7C4.6 9.3 0.7 5.4 0.4 1.8z"/></svg>
        677.258.4410
      </li>
      <li class="contact-item">
        <svg class="contact-icon" viewBox="0 0 10 10"><path d="M0.5 2h9v6h-9z M1.3 2.6L5 5.4l3.7-2.8" fill-rule="evenodd"/><path d="M1 2.5L5 5.5 9 2.5" stroke="#efeef2" stroke-width="0.7" fill="none"/></svg>
        plowana@krmortar.com
      </li>
      <li class="contact-item">
        <svg class="contact-icon" viewBox="0 0 10 10"><circle cx="5" cy="5" r="4.5"/><path d="M0.5 5h9 M5 0.5v9 M5 0.5c-2.4 2.4-2.4 6.6 0 9 M5 0.5c2.4 2.4 2.4 6.6 0 9" stroke="#efeef2" stroke-width="0.6" fill="none"/></svg>
        www.krmortar.com
      </li>
    </ul>
  </section>
</body>
</html>
```